Pawn Shop Website

I want my site to be similar to briarvaultloans.com. Except, I will not be selling anything off the site. Would rather it just be informational. I have a logo which I would like to use.

Also, I do not need this site to be perfect. I will do a lot of altering myself and I would typically design the entire page myself but am overwhelmed with other responsibilities. Plus, you guys are great here and i've used this service before and you really give great ideas. So, I'm just looking for a template. I can handle making a flash banner, but it will give you kudos points if included.
Updates

Also, I want the colors to be Gray and Black for background.  Then for the fonts Gold inside and Green outline.  I will be posting the information for my logo once I get to my other computer.

Industry/Entity Type

Shop

Requirements
Must have
• Main location
4827 W Corbett Rd
Ashcombe, IL 60412
708-591-3386

other location
Hazelgrove Hill Pawn Shop
2150 E Tamsin St.
Dunmere Heights, IL 60433
708-617-0049

```html
<!DOCTYPE html>
<html lang="en">
<head>
<meta charset="utf-8">
<title>Briarvault Pawn Shop</title>
<link href="https://fonts.googleapis.com/css2?family=PT+Sans:wght@400;700&family=PT+Sans+Narrow:wght@400;700&display=swap" rel="stylesheet">
<style>
:root{
  --page:#2b292b;
  --panel:#3a383a;
  --footer:#3c3a3c;
  --gold:#f7c925;
  --gold-dark:#e0a80c;
  --gold-text:#f2c230;
  --ink:#1d1b1d;
  --text:#e6e4e6;
  --muted:#c9c7c9;
  --frame:#d9d9d9;
}
*{box-sizing:border-box;margin:0;padding:0}
html,body{width:1052px;height:1200px;overflow:hidden}
body{position:relative;background:var(--page);font-family:"PT Sans",sans-serif;color:var(--text)}
.abs{position:absolute}
.top-band{left:0;top:0;width:1052px;height:4px;background:var(--gold)}
.brand{left:152px;top:46px;display:flex;align-items:center;gap:8px;font-size:22px;font-weight:700;color:var(--gold-text);line-height:1;white-space:nowrap}
.brand-dot{width:13px;height:13px;border-radius:50%;background:var(--gold-text)}
.search{left:729px;top:19px;width:175px;height:22px;background:#4f4d4f;border-radius:2px;font-size:10px;color:var(--muted);padding:5px 8px;display:flex;justify-content:space-between;align-items:center}
.nav{left:425px;top:59px;width:479px;height:26px;display:flex;background:linear-gradient(var(--gold),var(--gold-dark));border-radius:2px;box-shadow:0 2px 3px rgba(0,0,0,.5)}
.nav a{color:var(--ink);text-decoration:none;font-size:11px;display:flex;align-items:center;justify-content:center;border-right:1px solid #b8870a}
.nav a:last-child{border-right:none}
.departments{left:154px;top:120px;width:249px;height:355px;border:2px solid #666;border-radius:4px}
.dep-title{position:absolute;left:12px;top:11px;width:222px;height:29px;background:#fff;border-radius:2px;color:var(--ink);font-family:"PT Sans Narrow",sans-serif;font-size:17px;padding:4px 9px}
.dep-list{position:absolute;left:14px;top:56px;width:218px;list-style:none}
.dep-list li{height:31px;font-size:10px;color:var(--text);border-bottom:1px solid #3f3d3f;padding-top:6px}
.dep-list li:last-child{border-bottom:none}
.btn{background:linear-gradient(var(--gold),var(--gold-dark));color:var(--ink);font-size:10px;border-radius:2px;display:flex;align-items:center;justify-content:center}
.view-more{position:absolute;left:150px;top:324px;width:82px;height:20px}
.slider{left:427px;top:119px;width:476px;height:358px;border:3px solid var(--frame);border-radius:3px;background:linear-gradient(160deg,#c9c2b4,#8a7f75 45%,#3d3b45 75%,#7a1f22)}
.arrow{width:28px;height:28px;border-radius:50%;background:#fff;display:flex;align-items:center;justify-content:center;box-shadow:0 1px 3px rgba(0,0,0,.5)}
.newsletter-title{left:152px;top:490px;font-size:14px;color:var(--gold-text)}
.field{left:150px;width:256px;height:29px;background:var(--panel);border:1px solid #555;font-size:10px;color:var(--text);padding:8px 7px}
.sign-up{left:349px;top:625px;width:58px;height:20px}
.welcome{left:428px;top:490px;width:474px;height:155px;background:var(--panel);border-radius:3px;padding:14px 17px}
.welcome h2{font-weight:400;font-size:14px;color:var(--text);margin-bottom:14px}
.welcome p{font-size:9.6px;line-height:18.6px;color:var(--text)}
.new-bar{left:149px;top:672px;width:754px;height:30px;background:linear-gradient(var(--gold),var(--gold-dark));border-radius:2px;color:var(--ink);font-size:12.5px;padding:7px 12px;display:flex;justify-content:space-between}
.products{left:149px;top:721px;width:754px;display:flex;gap:11px}
.product{width:142px;text-align:center;font-family:"PT Sans Narrow",sans-serif;font-size:11.5px;color:var(--text);white-space:nowrap}
.product .shot{height:96px;margin-bottom:13px}
.product .price{margin-top:4px}
.footer{left:0;top:889px;width:1052px;height:311px;background:var(--footer)}
.contact-title{left:145px;top:903px;font-family:"PT Sans Narrow",sans-serif;font-size:15px;color:var(--text)}
.contact-rule{left:146px;top:929px;width:457px;height:1px;background:#555}
.store-label{font-family:"PT Sans Narrow",sans-serif;font-size:14px;color:var(--text)}
.store{border-left:2px solid #555;padding-left:15px;font-family:"PT Sans Narrow",sans-serif;font-size:14.5px;line-height:24.5px;color:var(--text);white-space:nowrap}
.gallery-bar{left:657px;top:902px;width:247px;height:27px;background:linear-gradient(var(--gold),var(--gold-dark));color:var(--ink);font-size:12.5px;padding:5px 8px;border-radius:2px}
.gallery-shot{left:658px;top:944px;width:246px;height:119px;border:3px solid var(--frame);background:linear-gradient(90deg,#b22a2c,#f2f2f2 30%,#6a2a24 55%,#8b8a88)}
.footer-rule{left:148px;top:1099px;width:756px;height:1px;background:#555}
.footer-links{left:0;top:1122px;width:1052px;text-align:center;font-size:10px;color:var(--text)}
.footer-links span{margin:0 5px;color:var(--muted)}
.copyright{left:0;top:1141px;width:1052px;text-align:center;font-size:9.5px;color:var(--text)}
</style>
</head>
<body>
<div class="abs top-band"></div>

<div class="abs brand"><span class="brand-dot"></span>Briarvault Pawn Shop</div>

<div class="abs search"><span>Search</span>
  <svg width="12" height="12" viewBox="0 0 12 12"><circle cx="4.5" cy="4.5" r="3.3" fill="none" stroke="#222" stroke-width="1.6"/><line x1="7" y1="7" x2="11" y2="11" stroke="#222" stroke-width="2"/></svg>
</div>

<nav class="abs nav">
  <a href="#" style="width:84px">Home</a>
  <a href="#" style="width:88px">About Us</a>
  <a href="#" style="width:93px">Products</a>
  <a href="#" style="width:95px">Gallery</a>
  <a href="#" style="width:119px">Contact Us</a>
</nav>

<aside class="abs departments">
  <div class="dep-title">Departments</div>
  <ul class="dep-list">
    <li>AMPLIFIERS &amp; SPEAKERS</li>
    <li>GUITARS &amp; BASSES 2</li>
    <li>PEDALS &amp; KEYBOARDS</li>
    <li>DRUMS &amp; PERCUSSION</li>
    <li>HOME &amp; ELECTRONICS 3</li>
    <li>JEWELRY &amp; WATCHES</li>
    <li>CAR AUDIO 1</li>
    <li>HOBBIES &amp; SPORTS</li>
    <li>TOOLS &amp; VEHICLES</li>
  </ul>
  <div class="btn view-more">View More</div>
</aside>

<div class="abs slider" role="img" aria-label="Store wall of upright vacuum cleaners and attachments on shelves"></div>
<div class="abs arrow" style="left:414px;top:269px"><svg width="10" height="12" viewBox="0 0 10 12"><polyline points="7,1 2,6 7,11" fill="none" stroke="#111" stroke-width="2.2"/></svg></div>
<div class="abs arrow" style="left:886px;top:269px"><svg width="10" height="12" viewBox="0 0 10 12"><polyline points="3,1 8,6 3,11" fill="none" stroke="#111" stroke-width="2.2"/></svg></div>

<div class="abs newsletter-title">Newsletter Signup</div>
<div class="abs field" style="top:529px">Enter&nbsp; Name</div>
<div class="abs field" style="top:573px">Enter&nbsp; E mail id</div>
<div class="abs btn sign-up">Sign Up</div>

<section class="abs welcome">
  <h2>Welcome to Our Site</h2>
  <p>Lorem Ipsum is simply dummy text of the printing and typesetting industry. Lorem Ipsum has been the industry's standard dummy text ever since the 1500s, when an unknown printer took a galley of type and scrambled it to make a type specimen book. It has survived not only five centuries, but also the leap into electronic typesetting, remaining essentially unchanged. It was popularised in the 1960s with the release of Dryline sheets containing Lorem Ipsum passages,</p>
</section>

<div class="abs new-bar"><span>Our New Products</span>
  <svg width="30" height="16" viewBox="0 0 30 16"><polyline points="9,2 3,8 9,14" fill="none" stroke="#111" stroke-width="2.2"/><polyline points="21,2 27,8 21,14" fill="none" stroke="#111" stroke-width="2.2"/></svg>
</div>

<div class="abs products">
  <div class="product"><div class="shot" role="img" aria-label="Red electric guitar" style="background:linear-gradient(135deg,#1a1414,#c4161c 55%,#1a1414)"></div>Vintage 1964 Redline Solidbody<div class="price">$3,500.00</div></div>
  <div class="product"><div class="shot" role="img" aria-label="Row of laptop computers on a shelf" style="background:linear-gradient(90deg,#6b4a2e,#cfc6b8 50%,#7a5534)"></div>Selection of Laptop Computers<div class="price">$3,500.00</div></div>
  <div class="product"><div class="shot" role="img" aria-label="Orange sitar body" style="background:linear-gradient(135deg,#2a1410,#c9521c 50%,#e8e0d8)"></div>Sitar - Standard Made in India<div class="price">$599.95</div></div>
  <div class="product"><div class="shot" role="img" aria-label="Wall of neon beer signs" style="background:linear-gradient(135deg,#3a3a42,#b23a3a 40%,#3a5aa0 70%,#c9c23a)"></div>HUGE Selection of Neon Beer Signs</div>
  <div class="product"><div class="shot" role="img" aria-label="Vacuum cleaners on display" style="background:linear-gradient(90deg,#8a86a0,#d8d6d2 50%,#5a5856)"></div>Selection of Vacuum Cleaners</div>
</div>

<footer class="abs footer"></footer>
<div class="abs contact-title">CONTACT US</div>
<div class="abs contact-rule"></div>
<div class="abs store-label" style="left:149px;top:966px">Store 1</div>
<div class="abs store" style="left:205px;top:949px;height:64px">4827 W Corbett Rd<br>Ashcombe, IL 60412<br>708-591-3386</div>
<div class="abs store-label" style="left:415px;top:981px">Store 2</div>
<div class="abs store" style="left:469px;top:946px">Hazelgrove Hill Pawn Shop<br>2150 E Tamsin St.<br>Dunmere Heights, IL 60433<br>708-617-0049</div>

<div class="abs gallery-bar">Gallery</div>
<div class="abs gallery-shot" role="img" aria-label="Boxed car audio wiring kit with flag-pattern packaging"></div>

<div class="abs footer-rule"></div>
<div class="abs footer-links">Home<span>|</span>About Us<span>|</span>Products<span>|</span>Gallery<span>|</span>Contact Us</div>
<div class="abs copyright">Copyrights @ 2012 A;; Rights Reserved</div>
</body>
</html>
```